Business card for a young aspring actress

My daughter is 18 and just starting out on her profession as an actress. She is a member of the Open Stage Company and has already had some extras work and a featured role in an upcoming Feature film.

She wants/needs a card that she can have to hand to give to those she comes into contact with in the theatre, TV and film industries.

We are thinking that it may be double sided with an impact side including a picture of her and her name etc with the reverse holding contact and other details.

She wants to go by the name Maren Joy Whitcombe.

She has done a little modelling but sees herself as an actress.

She can be seen in this video
http://www.hollybankacademy.example/videos/a3f19c7d5e2b8406c1d9e7f2a4b60835?width=640&height=480

Target Market(s)

Anyone she comes into contact with in theatre TV and film industries.

Industry/Entity Type

Business

Requirements
Nice to have
• She has email and a website www.marenwhitcombe.example She is quite a connected girl

```html
<!DOCTYPE html>
<html lang="en">
<head>
<meta charset="utf-8">
<title>Maren Joy Whitcombe — Business Card</title>
<link rel="stylesheet" href="https://fonts.googleapis.com/css2?family=Stint+Ultra+Condensed&family=Cormorant+Garamond:wght@400&family=Quicksand:wght@400&display=swap">
<style>
  :root {
    --canvas: #f4f4f4;
    --card-white: #ffffff;
    --ink-grey: #6b6b6b;
    --band-blue: #1ea3da;
    --photo-light: #e6e6e6;
    --photo-mid: #a9a9a9;
    --photo-dark: #4a4a4a;
    --accent-blue: #9fd3ea;
  }
  * { box-sizing: border-box; margin: 0; padding: 0; }
  html, body { width: 1200px; height: 960px; overflow: hidden; background: var(--canvas); }
  .canvas {
    width: 1200px; height: 960px;
    display: flex; flex-direction: column; align-items: center; justify-content: center;
    gap: 56px;
  }
  .card {
    width: 700px; height: 400px; position: relative; overflow: hidden;
    box-shadow: 0 6px 24px rgba(0,0,0,0.12);
  }
  /* Front: portrait side */
  .card--front { background: var(--photo-mid); }
  .card__portrait {
    position: absolute; inset: 0;
    background:
      radial-gradient(ellipse 38% 60% at 50% 55%, var(--photo-light) 0%, #cfcfcf 55%, transparent 80%),
      linear-gradient(90deg, var(--photo-dark) 0%, var(--photo-mid) 22%, var(--photo-mid) 78%, var(--photo-dark) 100%);
  }
  .card__portrait-accent {
    position: absolute; left: 18%; right: 18%; top: 36%; height: 28%;
    background: linear-gradient(90deg, transparent, var(--accent-blue) 30%, var(--accent-blue) 70%, transparent);
    opacity: 0.35;
  }
  .card__front-name {
    position: absolute; left: 0; right: 0; top: 47%;
    text-align: center;
    font-family: "Cormorant Garamond", serif;
    font-size: 34px; letter-spacing: 2px;
    color: var(--ink-grey);
  }
  /* Back: contact side */
  .card--back { background: var(--card-white); }
  .card__name {
    position: absolute; left: 0; right: 0; top: 92px;
    text-align: center;
    font-family: "Stint Ultra Condensed", serif;
    font-size: 62px; color: var(--ink-grey);
    letter-spacing: 0.5px;
  }
  .card__contact-band {
    position: absolute; left: 0; right: 0; bottom: 0; height: 118px;
    background: var(--band-blue);
    display: flex; align-items: center; justify-content: space-between;
    padding: 0 48px;
    font-family: "Quicksand", sans-serif;
    font-size: 13px; color: var(--card-white); letter-spacing: 0.3px;
  }
  .card__divider { width: 1px; height: 12px; background: var(--card-white); opacity: 0.85; }
</style>
</head>
<body>
<main class="canvas">
  <section class="card card--front">
    <div class="card__portrait" role="img" aria-label="Black and white close-up portrait of the actress with soft blue brush lettering of her surname across the eyes"></div>
    <div class="card__portrait-accent"></div>
    <p class="card__front-name">MAREN JOY</p>
  </section>

  <section class="card card--back">
    <h1 class="card__name">Maren Joy Whitcombe</h1>
    <div class="card__contact-band">
      <span class="card__contact">www.marenwhitcombe.example</span>
      <span class="card__divider"></span>
      <span class="card__contact">maren@marenwhitcombe.example</span>
      <span class="card__divider"></span>
      <span class="card__contact">012 98 76 54 32</span>
    </div>
  </section>
</main>
</body>
</html>
```